Around the world sailing blogger needs a book cover template designed

Hello. I'm interested in writing a series of 'guides' in relation to sailing and live-aboard cruising. Last April my husband and I sold all our possessions and purchased the largest boat we could find. Since then I've been sailing and blogging about our experiences and am slowing building up a popular website and shop. The first guide in my series is finished. It's a guide to using the VHF radio with checklist templates for the user to use. The next guide might have something to do with maintenance checklists (engine, generator, water maker, etc). Anyway, I need a cover that will act as a template for future guides so it needs to have nautical imagery, a headline, subhead, author, my logo and perhaps a quote or something and it needs to be replicated across the series. In other words it needs to be created in a way that we (or should I say you) can make more covers easily with the same look and feel. The cover needs to be created for PDF, Readly (electronic) PrintHarbor (hardcopy) at the very least... And I'll also need some thumbnails for promotional purposes. The imagery on this first one needs to cover communication/VHF radio/Sailing... I know it sounds like a boring book but it will be very useful to the user. And I really need the cover to look awesome :) To see my website it's at DriftwoodNomad.com. Final note - I've never used Pixel Forum before so this is my first time. I'm not sure if I've given you everything you need...Also, I need more than just a cover. Hopefully I can find someone that can help me with all my books and digital products that I have lined up. I'll stop typing now :)

I've just added of some pictures of our boat while we're sailing it. They might make a nice cover - I don't know. I'm really sorry for not providing this to begin with... I've never used this service before so I'm trialling it to see if it's better/easier than hirePod. I know it's really frustrating when someone wants something and doesn't give all the information up front. I just didn't understand how this all works so I apologise. I have thousands of photos...these were taken by a professional so I'm hoping they're the best... Also, keep in mind I'm looking for a series of guides and this one is on VHF radio...I can't have a photo of our boat for every guide. Next time I post a project I'll be far more knowledgable. Sorry for any inconvenience. That being said, if we do use a photo of the back of the boat, the logo is already there so we don't need the logo twice... Jo

Target Market(s)

Sailors, boaters, full time boaters...sailors sailing around the world. Anyone that owns a boat and a VHF radio. Both men and women... English speaking. Biggest audience in USA then UK, Australian, NZ, Europe..

Industry/Entity Type

Building

Font styles to use
Serif
Sans Serif

Requirements
Must have
• My logo, headlines, subhead, author line and good imagery. Using a VHF is rather boring but my book offers templates so that users can easily fill out a MAYDAY (SOS) form and feel confident when they have to broadcast the information across the radio. It an idiots guide to VHF radios...A lot of people are nervous about using them when they first start out - especially women - so this guide will help reduce anxiety.
Nice to have
• Colours that match my website might be too much blue - might be nice to have some different colors?

```html
<!DOCTYPE html>
<html lang="en">
<head>
<meta charset="utf-8">
<title>Generators and Engines – Beginners Guide to Sailing, Part Two</title>
<link rel="stylesheet" href="https://fonts.googleapis.com/css2?family=Archivo+Black&family=Arimo:wght@700&family=Cormorant+Garamond:wght@500&display=swap">
<style>
  :root {
    --paper: #ffffff;
    --navy: #1c3d6e;
    --ink: #0d0d0d;
    --gold-light: #f3d77a;
    --gold-mid: #c9962f;
    --gold-deep: #7a5413;
  }
  * { margin: 0; padding: 0; box-sizing: border-box; }
  html, body { width: 816px; height: 1200px; overflow: hidden; background: var(--paper); }
  .cover { position: relative; width: 816px; height: 1200px; background: var(--paper); overflow: hidden; }

  .series-title {
    position: absolute; left: 0; right: 0; top: 28px;
    text-align: center; color: var(--navy);
    font-family: "Arimo", Arial, sans-serif; font-weight: 700;
    letter-spacing: 3px;
  }
  .series-title .line { display: block; font-size: 31px; line-height: 52px; }
  .series-title .part { display: block; font-size: 22px; line-height: 40px; margin-top: 4px; }

  .brand-mark {
    position: absolute; left: 350px; top: 172px; width: 120px; height: 120px;
    border: 2px solid var(--navy); border-radius: 50%;
    display: flex; align-items: center; justify-content: center; text-align: center;
    font-family: "Arimo", Arial, sans-serif; font-weight: 700; font-size: 14px;
    line-height: 18px; color: var(--navy); letter-spacing: 1px;
  }

  .wheel-art { position: absolute; left: 0; top: 0; width: 816px; height: 1200px; }

  .headline {
    position: absolute; right: 48px; top: 512px; text-align: right;
    font-family: "Archivo Black", "Arial Black", sans-serif;
    font-size: 51px; line-height: 46px; color: var(--ink); letter-spacing: 1px;
  }
  .subhead {
    position: absolute; right: 48px; top: 624px; text-align: right;
    font-family: "Arimo", Arial, sans-serif; font-weight: 700;
    font-size: 42px; line-height: 43px; color: var(--navy); letter-spacing: 1px;
  }

  .author {
    position: absolute; left: 0; right: 0; top: 1108px; text-align: center;
    font-family: "Cormorant Garamond", Georgia, serif; font-weight: 500;
    font-size: 40px; letter-spacing: 9px; color: var(--navy);
  }
</style>
</head>
<body>
<main class="cover">
  <svg class="wheel-art" viewBox="0 0 816 1200" role="img" aria-label="Illustration of a polished brass ship's wheel with a marine engine and a handheld VHF radio set between its spokes">
    <defs>
      <radialGradient id="brass" cx="0.35" cy="0.4" r="0.75">
        <stop offset="0" stop-color="var(--gold-light)"/>
        <stop offset="0.55" stop-color="var(--gold-mid)"/>
        <stop offset="1" stop-color="var(--gold-deep)"/>
      </radialGradient>
    </defs>
    <circle cx="0" cy="705" r="360" fill="url(#brass)"/>
  </svg>

  <header class="series-title">
    <span class="line">A COMPREHENSIVE BEGINNERS</span>
    <span class="line">GUIDE TO SAILING</span>
    <span class="part">PART TWO</span>
  </header>

  <div class="brand-mark">DRIFTWOOD<br>NOMAD</div>

  <h1 class="headline">GENERATORS<br>AND ENGINES</h1>
  <h2 class="subhead">FINDING FAULTS<br>AND<br>MAINTENENCE<br>FOR<br>SAILORS</h2>

  <p class="author">ROSALIND MAE CARTER</p>
</main>
</body>
</html>
```